eMira7: Web Landing / Homepage (Design Only / Logo Supplied!)

Landing / Homepage
(Design Only / Logo Supplied!)

eMira7 should be just what it looks like as in a resemblance of the logo for Vorto qBolt.

The real logo aspect should be the adaptation of the universal symbol for infinity incorporated with a directional arrow indicating infinite motion.

This should be incorporated with the eMira7/Infinity Sign

- Overview / Background of the Business

Recently I was bullied out of a job and it ruined my life, temporarily. Everything was taken from me, my self esteem, my finances, my emotional and physical health. I decided to start a diversity and social sustainability consulting firm.

The primary goal of my business is to promote ethnic/social/cultural diversity and equality in the workplace. I am going to do public speaking engagements and consulting with companies on how to develop more inclusive policies in the workplace.

- The Target Market / Audience we are trying to reach

My target market is those who would align themselves with social/economic progressives, Harbor Tent Rising sympathisers and others who value political and economic equality and would like to change issues such as economic, gender, racial, and class equality issues.

- Design Specifics; preferences or ideas for Style, Colour, Font, Imagery, etc

Only Black, Grey, or Dark Blue. Please see the attachment for the infinity sign for ideas of where to start the design and incorporate it in with

- Content to be included in the web design

We require a Homepage
The content will be structured as a interactive website for news, information, and support for people who have been marginalised, bullied, oppressed, and harassed and want to positively contribute back into society, instead of hurting themselves or others.

Target Market(s)

18-45 year old Bullying and Discrimination victims and those who are sensitive to those with mental health issues.

Industry/Entity Type

Sustainability

Requirements
Must have
• eMira7 and the infinity sign must be elegantly and smoothly integrated

It should focus on the colours black, blue, grey and be professional in look and feel.

Navigation and tone should be serious and feel like a news paper or serious news magazine outlook
Nice to have
• Rollovers leading to other sites about bullying, discrimination, gender bias and age discrimination.

The site should be as cross platform as possible.
Should not have
• Unknown at this time

```html
<!DOCTYPE html>
<html lang="en">
<head>
<meta charset="utf-8">
<title>eMira7 — Home</title>
<link href="https://fonts.googleapis.com/css2?family=Arimo:wght@400;700&family=Gelasio:wght@400&display=swap" rel="stylesheet">
<style>
:root{
  --page:#f7f8fa;
  --ink:#3a3a3a;
  --text:#555555;
  --muted:#777777;
  --rule:#cfcfcf;
  --dark:#3d3d3d;
  --dark-rule:#5e5e5e;
  --panel:#e9eaec;
  --panel-line:#d8d9db;
  --footer:#3f3f3f;
  --footer-text:#b9b9b9;
  --photo-a:#e3e6eb;
  --photo-b:#8d96a6;
}
*{box-sizing:border-box;margin:0;padding:0}
html,body{width:1128px;height:1200px;overflow:hidden}
body{background:var(--page);font-family:"Arimo",Arial,sans-serif;color:var(--text);position:relative}
.serif{font-family:"Gelasio",Georgia,serif}
.abs{position:absolute}

.brand{left:88px;top:98px;display:flex;align-items:center;gap:12px}
.brand-dot{width:22px;height:22px;border-radius:50%;background:var(--ink)}
.brand-name{font-size:38px;font-weight:400;color:var(--ink);letter-spacing:4px}
.tagline{left:287px;top:108px;font-size:11px;letter-spacing:4.6px;line-height:12.5px;color:var(--ink);text-align:center;width:208px}

.contact{right:84px;top:27px;text-align:right;font-size:14px;color:var(--text);line-height:32px}
.search{left:885px;top:95px;width:158px;height:33px;border:1px solid #d3d3d3;background:#fff;border-radius:2px;box-shadow:0 1px 2px rgba(0,0,0,.12)}
.search span{position:absolute;left:12px;top:10px;font-size:11px;color:#aaa;font-style:italic}
.search svg{position:absolute;right:10px;top:10px}

.nav{left:85px;top:165px;width:960px;height:52px;border-top:1px solid var(--rule);border-bottom:1px solid var(--rule)}
.nav a{position:absolute;top:0;height:50px;line-height:50px;font-size:15px;color:var(--ink);text-decoration:none;transform:translateX(-50%)}
.nav .current{top:8px;height:36px;line-height:36px;width:100px;background:var(--dark);color:#fff;border-radius:2px;text-align:center;transform:none}
.nav .sep{position:absolute;top:8px;width:1px;height:36px;background:var(--rule)}

.hero{left:84px;top:228px;width:961px;height:288px;background:#e6e7e9;padding:5px}
.hero-inner{position:relative;width:100%;height:100%;background:#f4f5f7;overflow:hidden}
.hero-photo{position:absolute;right:0;top:0;width:520px;height:100%;background:linear-gradient(90deg,var(--page) 0%,var(--photo-a) 25%,var(--photo-b) 100%)}
.hero h1{position:absolute;left:36px;top:40px;font-size:29px;font-weight:400;color:#555}
.hero p{position:absolute;left:36px;top:92px;width:400px;font-size:12px;line-height:22px;color:var(--muted)}
.btn{display:inline-block;background:var(--dark);color:#fff;font-size:14px;padding:0 14px;height:33px;line-height:33px;border-radius:2px}
.hero .btn{position:absolute;left:39px;top:167px}
.dots{position:absolute;right:28px;bottom:24px;display:flex;gap:14px}
.dots i{display:block;width:16px;height:16px;border-radius:50%;background:rgba(255,255,255,.55)}
.dots i.on{background:var(--dark);border:2px solid #fff}

.feature{top:529px;width:316px;height:135px;background:var(--panel);border:1px solid var(--panel-line)}
.feature .pic{position:absolute;left:8px;top:9px;width:113px;height:115px}
.feature h3{position:absolute;left:137px;top:16px;font-size:13px;font-weight:400;color:var(--ink)}
.feature p{position:absolute;left:137px;top:40px;width:170px;font-size:11.5px;line-height:18px;color:var(--text);text-align:justify}
.feature a,.more{font-family:"Gelasio",Georgia,serif;font-size:14px;color:var(--ink);text-decoration:underline}
.feature a{position:absolute;right:13px;top:102px}

.news{left:85px;top:687px;width:246px;height:381px;background:var(--dark);border-radius:2px;color:#fff}
.news-head{position:absolute;left:5px;right:5px;top:0;height:48px;border-bottom:1px solid var(--dark-rule)}
.news-head svg{position:absolute;left:10px;top:15px}
.news-head span{position:absolute;left:43px;top:12px;font-size:18px}
.news-item{position:absolute;left:18px;width:220px}
.news-item h4{font-size:13px;font-weight:400;padding-left:19px;position:relative}
.news-item h4:before{content:"";position:absolute;left:0;top:3px;border-left:6px solid #fff;border-top:4px solid transparent;border-bottom:4px solid transparent}
.news-item p{padding-left:19px;margin-top:8px;font-size:11.5px;line-height:18px;color:#c4c4c4}

.article{left:358px;width:687px}
.article h2{font-size:18px;font-weight:400;color:var(--ink)}
.article p{margin-top:17px;font-size:11.5px;line-height:23.5px;color:var(--text);text-align:justify}
.article .more{display:inline-block;margin-top:8px}
.divider{left:358px;top:877px;width:687px;height:1px;background:var(--rule)}

.footer{left:0;top:1088px;width:1128px;height:112px;background:var(--footer)}
.footer-nav{position:absolute;left:85px;top:32px;font-size:12px;color:var(--footer-text)}
.footer-nav b{font-weight:400;margin:0 8px}
.copy{position:absolute;left:85px;top:64px;font-size:12px;color:var(--footer-text);word-spacing:2px}
.social{position:absolute;left:921px;top:44px;display:flex;gap:9px}
.social i{display:block;width:24px;height:24px;border-radius:50%;background:#6e6e6e;position:relative}
.social svg{position:absolute;left:5px;top:6px}
</style>
</head>
<body>

<header>
  <div class="abs brand"><span class="brand-dot"></span><span class="brand-name">eMira7</span></div>
  <div class="abs tagline">social justice<br>social sustainability<br>social inclusion</div>
  <div class="abs contact">Call us :&nbsp; 555 214 3870<br>E mail&nbsp; :&nbsp; info@emira7.com</div>
  <div class="abs search"><span>Search</span>
    <svg width="11" height="11" viewBox="0 0 11 11"><circle cx="4.5" cy="4.5" r="3.3" fill="none" stroke="#bbb" stroke-width="1.3"/><line x1="7" y1="7" x2="10" y2="10" stroke="#bbb" stroke-width="1.5"/></svg>
  </div>
</header>

<nav class="abs nav">
  <a class="current serif" style="left:22px">Home</a>
  <span class="sep" style="left:114px"></span>
  <a class="serif" style="left:178px">About us</a>
  <span class="sep" style="left:246px"></span>
  <a class="serif" style="left:302px">Services</a>
  <span class="sep" style="left:365px"></span>
  <a class="serif" style="left:422px">Project</a>
  <span class="sep" style="left:482px"></span>
  <a class="serif" style="left:538px">Budget</a>
  <span class="sep" style="left:598px"></span>
  <a class="serif" style="left:658px">Partners</a>
  <span class="sep" style="left:723px"></span>
  <a class="serif" style="left:789px">Contact us</a>
  <span class="sep" style="left:856px"></span>
  <a class="serif" style="left:909px">Help</a>
</nav>

<section class="abs hero">
  <div class="hero-inner">
    <div class="hero-photo" role="img" aria-label="Photo of smiling business people applauding in a row"></div>
    <h1 class="serif">Welcome to our site</h1>
    <p>Sed et ultrices urna. Pellentesque id fringilla lacus. Vestibulum enim nunc, euismod et posuere eget, adipiscing sit amet nibh. Nullam placerat eros eros. Aenean sed ligula in leo viverra malesuada.</p>
    <span class="btn serif">View more</span>
    <div class="dots"><i class="on"></i><i></i><i></i><i></i></div>
  </div>
</section>

<article class="abs feature" style="left:84px">
  <div class="pic" role="img" aria-label="Photo of men in suits at an outdoor public event" style="background:linear-gradient(160deg,#c9d3de,#3b4251)"></div>
  <h3>Maecen vehicula scelerisque</h3>
  <p>Adipiscing sit amet nibh. Nullam placerat eros eros. Aenean sed ligula in leo viverra.</p>
  <a>View more</a>
</article>
<article class="abs feature" style="left:407px">
  <div class="pic" role="img" aria-label="Photo of riot police confronting a protester" style="background:linear-gradient(160deg,#8a847a,#3a3833)"></div>
  <h3>Maecen vehicula scelerisque</h3>
  <p>Adipiscing sit amet nibh. Nullam placerat eros eros. Aenean sed ligula in leo viverra.</p>
  <a>View more</a>
</article>
<article class="abs feature" style="left:729px">
  <div class="pic" role="img" aria-label="Photo of a street with small fires during a protest" style="background:linear-gradient(160deg,#b9b3aa,#6e5e4e)"></div>
  <h3>Maecen vehicula scelerisque</h3>
  <p>Adipiscing sit amet nibh. Nullam placerat eros eros. Aenean sed ligula in leo viverra.</p>
  <a>View more</a>
</article>

<aside class="abs news">
  <div class="news-head">
    <svg width="20" height="16" viewBox="0 0 20 16"><rect x="0.5" y="0.5" width="19" height="15" fill="none" stroke="#fff"/><rect x="3" y="3" width="6" height="5" fill="#fff"/><line x1="11" y1="4" x2="17" y2="4" stroke="#fff"/><line x1="11" y1="7" x2="17" y2="7" stroke="#fff"/><line x1="3" y1="10.5" x2="17" y2="10.5" stroke="#fff"/><line x1="3" y1="13" x2="17" y2="13" stroke="#fff"/></svg>
    <span class="serif">Latest News</span>
  </div>
  <div class="news-item" style="top:68px"><h4>Maecen vehicula scelerisque</h4><p>Nullam placerat eros eros. Aenean sed ligula in leo viverra.</p></div>
  <div class="news-item" style="top:147px"><h4>Maecen vehicula scelerisque</h4><p>Nullam placerat eros eros. Aenean sed ligula in leo viverra.</p></div>
  <div class="news-item" style="top:227px"><h4>Maecen vehicula scelerisque</h4><p>Nullam placerat eros eros. Aenean sed ligula in leo viverra.</p></div>
  <div class="news-item" style="top:306px"><h4>Maecen vehicula scelerisque</h4><p>Nullam placerat eros eros. Aenean sed ligula in leo viverra.</p></div>
</aside>

<section class="abs article" style="top:700px">
  <h2 class="serif">What project would you like to develop?</h2>
  <p>I would like the project to develop and to utilizecurrent Internet, digital technologies and social media to create a template for alternatively abled person's to report the news by themselves and for themselves. This would enrich their lives and the lives of others around them, creating a more social sustainable community. eMira7will create a fully scalable, replicable, and commercially viable model well within the 16-week deadline period.</p>
  <a class="more">View more</a>
</section>
<div class="abs divider"></div>
<section class="abs article" style="top:899px">
  <h2 class="serif">Audience: who would your project impact, assist or reach?</h2>
  <p>The potential audience is very diverse and it has the ability to reach, impact, and assist the global community in ways CivicLoop may not have begun to realize. The people who will be impacted are those who are being influenced by decisions of bureaucrats making funding decisions for schools, libraries and communities around Queensland. From the viewpoint of a non-whitenon-European immigrant the average Australian world-viewcan unfairly appear to be extremely myopic bordering on parochial.</p>
  <a class="more">View more</a>
</section>

<footer class="abs footer">
  <div class="footer-nav">Home<b>|</b>About us<b>|</b>Services<b>|</b>Project<b>|</b>Budget<b>|</b>Partners<b>|</b>Contact us<b>|</b>Help</div>
  <div class="copy">Copyright ©&nbsp; 2012&nbsp; www.emira7.com&nbsp;&nbsp; All rights reserved.</div>
  <div class="social">
    <i></i><i></i><i></i>
    <i><svg width="14" height="11" viewBox="0 0 14 11"><rect x="0.5" y="0.5" width="13" height="10" fill="none" stroke="#ddd"/><polyline points="0.5,0.5 7,6 13.5,0.5" fill="none" stroke="#ddd"/></svg></i>
  </div>
</footer>

</body>
</html>
```